Lumora Learning Web Design Project

Who We are:
Lumora Learning is education information portal/ magazine, providing information about the Chinese and International education markets. Our aim is to help school principals improve there curriculum, and parents in understanding this curriculum.

Project Brief:
The site will include education news updates, educational services, curriculum developments and overseas study. We hope the site represents the cross cultural bridge between the west and east. The site will cover both the Sciences and Arts.

Note:
The logo design competition is also underway so we only need the website design

What We want:
This competition is for Design only no coding!
Design a home page based on Template 1,2 or 3. I only need to select one.
The design of an article page.

Optional
Design a Microsoft Windows metro style splash page.

Sites We like:
http://www.kavelin.com.cn/kavelinlingo/default.aspx
http://www.brixtalacademia.co.uk/
http://qrpv.norvatestudio.net/

Template Explanations:
Template 1-
The main information has a dynamic sliding category view that when clicked displays the relevant info.
In addition to the main upper menu it also has a left hand sliding menu that pops out on click or gesture

Template 2-
Has limited number of Articles most of the menus are drop downs from the top menu

Template 3-
No Top menu

Target Market(s)

Teachers, principals and parents

Industry/Entity Type

Education

Requirements
Should not have
• kindergarten preschool feel

```html
<!DOCTYPE html>
<html lang="en">
<head>
<meta charset="utf-8">
<title>Lumora Learning</title>
<link rel="stylesheet" href="https://fonts.googleapis.com/css2?family=Arimo&family=Noto+Serif:ital@0;1&family=Open+Sans&family=Signika:wght@300;400&display=swap">
<style>
:root{
  --ink:#222;
  --muted:#aaa;
  --rule:#ddd;
  --brand-blue:#235f92;
  --brand-red:#d9261c;
  --accent-blue:#2f6fc9;
  --cat-one:#a1181f;
  --cat-two:#06a9ce;
  --cat-three:#0c2a78;
  --cat-four:#fb5a3c;
  --cat-five:#741c85;
  --cat-six:#02a8a8;
  --cat-seven:#c5714a;
  --footer-bg:#f7f4f4;
  --bar-bg:#333;
}
*{box-sizing:border-box;margin:0;padding:0}
html,body{width:1200px;height:1172px;overflow:hidden;background:#fff}
body{position:relative;font-family:"Arimo",Arial,sans-serif;color:var(--ink);font-size:13px}
.abs{position:absolute}
.heading{font-family:"Signika",sans-serif;font-weight:300;font-size:25px;color:#333;line-height:1}
.brand-mark{border-radius:50%;background:var(--brand-blue)}
.brand-name{font-family:"Arimo",Arial,sans-serif;color:var(--brand-red);white-space:nowrap;letter-spacing:.5px}

/* header */
.search{left:869px;top:57px;width:290px;height:32px;border:1px solid #ddd;display:flex}
.search-field{flex:1;font-family:"Noto Serif",serif;font-style:italic;font-size:11px;color:#aaa;padding:9px 14px}
.search-button{width:58px;background:#f2f2f2;border-left:1px solid #ddd;font-size:12px;color:#555;text-align:center;line-height:30px}
.main-nav{left:440px;top:131px;display:flex}
.nav-item{padding:0 14px;border-left:1px dotted #ccc;height:36px}
.nav-item:first-child{border-left:none}
.nav-item b{display:block;font-weight:400;font-size:14px;color:#333}
.nav-item i{display:block;font-family:"Noto Serif",serif;font-size:11px;color:#aaa;margin-top:2px}
.nav-item.active b{color:var(--accent-blue)}
.header-rule{left:40px;top:196px;width:1120px;height:3px;background:var(--rule)}

/* side menu */
.side-menu{left:40px;top:260px;width:220px;list-style:none}
.side-menu>li{border-bottom:1px solid #eee;padding:7px 0 7px 18px;line-height:17px;position:relative}
.side-menu>li:last-child{border-bottom:none}
.side-menu li::before{content:"→";position:absolute;left:3px;color:#3aa0e0;font-size:9px}
.sub-menu{list-style:none;margin:3px 0 0 21px}
.sub-menu li{position:relative;line-height:20px}
.sub-menu li::before{left:-16px}

/* slider + categories */
.slider{left:280px;top:219px;width:640px;height:320px;background:var(--brand-blue)}
.dots{background-image:radial-gradient(#ddd 0.8px,transparent 1px);background-size:3px 3px}
.tile{position:absolute;color:#fff;font-family:"Open Sans",sans-serif;text-transform:uppercase;font-size:15px;line-height:17px;padding:7px 8px;letter-spacing:-.3px}
.tile.large{font-size:46px;line-height:46px;padding:8px 10px}
.tile.medium{font-size:31px;line-height:29px;padding:14px 14px}

/* blogs */
.blog-thumb{width:60px;height:60px;border:4px solid #eee}
.blog-title{font-size:12px;color:#333}
.blog-meta{font-family:"Noto Serif",serif;font-style:italic;font-size:10px;color:#aaa;display:flex;align-items:center;gap:6px}
.newsletter-input{left:944px;top:687px;width:214px;height:31px;border:1px solid #ddd}
.subscribe{left:1030px;top:731px;width:130px;height:30px;background:var(--brand-blue);color:#fff;font-family:"Signika",sans-serif;font-size:17px;text-align:center;line-height:30px}

/* footer */
.footer{left:0;top:898px;width:1200px;height:220px;background:var(--footer-bg);border-top:1px solid #ece6e6}
.follow-count{font-family:"Noto Serif",serif;font-size:12px;color:#999;display:flex;align-items:center;gap:6px}
.social-square{width:32px;height:32px}
.contents-col{list-style:none;font-size:12px;line-height:20px}
.address{left:960px;top:1019px;font-size:12.5px;line-height:20px}
.bottom-bar{left:0;top:1118px;width:1200px;height:54px;background:var(--bar-bg);color:#fff;font-size:14px;text-align:center;line-height:60px}
</style>
</head>
<body>

<header>
  <div class="abs brand-mark" style="left:142px;top:45px;width:80px;height:80px"></div>
  <div class="abs brand-name" style="left:60px;top:135px;font-size:25px">LUMORA LEARNING</div>

  <div class="abs search"><div class="search-field">to search, type and hit enter</div><div class="search-button">Search</div></div>

  <nav class="abs main-nav">
    <div class="nav-item active"><b>Home</b><i>welcome</i></div>
    <div class="nav-item" style="padding-left:23px;padding-right:24px"><b>About us</b><i>new on site</i></div>
    <div class="nav-item" style="padding-left:26px;padding-right:20px"><b>Some menu</b><i>description</i></div>
    <div class="nav-item" style="padding-left:19px;padding-right:24px"><b>Another menu</b><i>Description</i></div>
    <div class="nav-item" style="padding-left:23px;padding-right:20px"><b>Blogs</b><i>some description</i></div>
    <div class="nav-item" style="padding-left:19px"><b>contact us</b><i>We glad to assist</i></div>
  </nav>
  <div class="abs header-rule"></div>
</header>

<aside>
  <div class="abs heading" style="left:41px;top:220px">Menu title</div>
  <ul class="abs side-menu">
    <li>Menu item1</li>
    <li>Menu item2
      <ul class="sub-menu"><li>Sub menu</li><li>Sub menu</li><li>Sub menu</li><li>Sub menu</li><li>Sub menu</li></ul>
    </li>
    <li>Menu item3</li><li>Menu item4</li><li>Menu item5</li><li>Menu item6</li>
    <li>Menu item7</li><li>Menu item8</li><li>Menu item9</li>
    <li>Menu item2
      <ul class="sub-menu"><li>Sub menu</li><li>Sub menu</li><li>Sub menu</li><li>Sub menu</li><li>Sub menu</li></ul>
    </li>
  </ul>
</aside>

<main>
  <div class="abs slider" role="img" aria-label="Featured slide image"></div>

  <div class="abs heading" style="left:281px;top:563px">Categories</div>
  <div class="abs dots" style="left:407px;top:570px;width:512px;height:10px"></div>

  <div class="tile large" style="left:281px;top:605px;width:382px;height:174px;background:var(--cat-one)">Category<br>One</div>
  <div class="tile" style="left:666px;top:605px;width:125px;height:86px;background:var(--cat-two)">Category<br>Two</div>
  <div class="tile" style="left:794px;top:605px;width:125px;height:86px;background:var(--cat-three)">Category<br>Three</div>
  <div class="tile medium" style="left:666px;top:694px;width:253px;height:174px;background:var(--cat-seven)">Category<br>Seven</div>
  <div class="tile" style="left:281px;top:783px;width:125px;height:86px;background:var(--cat-four)">Category<br>Four</div>
  <div class="tile" style="left:410px;top:783px;width:125px;height:86px;background:var(--cat-five)">Category<br>Five</div>
  <div class="tile" style="left:538px;top:783px;width:125px;height:86px;background:var(--cat-six)">Category<br>Six</div>
</main>

<aside>
  <div class="abs heading" style="left:944px;top:222px">Recent blogs</div>

  <div class="abs blog-thumb" style="left:944px;top:274px"></div>
  <div class="abs blog-title" style="left:1024px;top:273px">Quisque libero semin</div>
  <div class="abs blog-meta" style="left:1024px;top:312px"><svg width="16" height="13"><path d="M0 0h16v10H6l-4 3v-3H0z" fill="#e6e6e6"/></svg>25 <span>|</span><svg width="15" height="13"><path d="M7.5 13L1 6.5A3.6 3.6 0 0 1 7.5 2a3.6 3.6 0 0 1 6.5 4.5z" fill="#e6e6e6"/></svg>20</div>

  <div class="abs blog-thumb" style="left:944px;top:354px"></div>
  <div class="abs blog-title" style="left:1024px;top:353px">Quisque libero semin</div>
  <div class="abs blog-meta" style="left:1024px;top:392px"><svg width="16" height="13"><path d="M0 0h16v10H6l-4 3v-3H0z" fill="#e6e6e6"/></svg>25 <span>|</span><svg width="15" height="13"><path d="M7.5 13L1 6.5A3.6 3.6 0 0 1 7.5 2a3.6 3.6 0 0 1 6.5 4.5z" fill="#e6e6e6"/></svg>20</div>

  <div class="abs blog-thumb" style="left:944px;top:435px"></div>
  <div class="abs blog-title" style="left:1024px;top:434px">Quisque libero semin</div>
  <div class="abs blog-meta" style="left:1024px;top:473px"><svg width="16" height="13"><path d="M0 0h16v10H6l-4 3v-3H0z" fill="#e6e6e6"/></svg>25 <span>|</span><svg width="15" height="13"><path d="M7.5 13L1 6.5A3.6 3.6 0 0 1 7.5 2a3.6 3.6 0 0 1 6.5 4.5z" fill="#e6e6e6"/></svg>20</div>

  <div class="abs blog-thumb" style="left:944px;top:516px"></div>
  <div class="abs blog-title" style="left:1024px;top:515px">Quisque libero semin</div>
  <div class="abs blog-meta" style="left:1024px;top:554px"><svg width="16" height="13"><path d="M0 0h16v10H6l-4 3v-3H0z" fill="#e6e6e6"/></svg>25 <span>|</span><svg width="15" height="13"><path d="M7.5 13L1 6.5A3.6 3.6 0 0 1 7.5 2a3.6 3.6 0 0 1 6.5 4.5z" fill="#e6e6e6"/></svg>20</div>

  <div class="abs dots" style="left:940px;top:600px;width:218px;height:18px"></div>

  <div class="abs heading" style="left:942px;top:642px">Newsletter</div>
  <div class="abs newsletter-input"></div>
  <div class="abs subscribe">Subscribe</div>
</aside>

<footer>
  <div class="abs footer"></div>

  <div class="abs heading" style="left:43px;top:926px">Follow us</div>
  <div class="abs follow-count" style="left:44px;top:973px"><svg width="17" height="17"><circle cx="8.5" cy="8.5" r="8" fill="#f39019"/></svg>3042</div>
  <div class="abs" style="left:109px;top:972px;height:18px;border-left:1px dotted #ccc"></div>
  <div class="abs follow-count" style="left:123px;top:973px"><svg width="24" height="17"><circle cx="11" cy="8.5" r="8" fill="#2fa6e6"/></svg>301</div>
  <div class="abs" style="left:195px;top:972px;height:18px;border-left:1px dotted #ccc"></div>
  <div class="abs follow-count" style="left:207px;top:973px;font-family:'Arimo',sans-serif"><svg width="17" height="17"><circle cx="8.5" cy="8.5" r="8" fill="#2a62d6"/></svg>800</div>

  <div class="abs social-square" style="left:40px;top:1020px;background:#3b5998" role="img" aria-label="Social profile link"></div>
  <div class="abs social-square" style="left:82px;top:1020px;background:#5eb6e3" role="img" aria-label="Social profile link"></div>
  <div class="abs social-square" style="left:124px;top:1020px;background:#f39019" role="img" aria-label="News feed link"></div>
  <div class="abs social-square" style="left:170px;top:1020px;background:#6cc4e6" role="img" aria-label="Video channel link"></div>
  <div class="abs social-square" style="left:212px;top:1020px;background:#0077b5" role="img" aria-label="Professional network link"></div>

  <div class="abs heading" style="left:281px;top:926px">Contents list</div>
  <ul class="abs contents-col" style="left:306px;top:961px"><li>Lorem ipsum dolor sit amet</li><li>Lorem ipsum dolor sit amet</li><li>Lorem ipsum dolor sit amet</li><li>Lorem ipsum dolor sit amet</li><li>Lorem ipsum dolor sit amet</li><li>Lorem ipsum dolor sit amet</li></ul>
  <ul class="abs contents-col" style="left:507px;top:961px"><li>Lorem ipsum dolor sit amet</li><li>Lorem ipsum dolor sit amet</li><li>Lorem ipsum dolor sit amet</li><li>Lorem ipsum dolor sit amet</li><li>Lorem ipsum dolor sit amet</li><li>Lorem ipsum dolor sit amet</li></ul>
  <ul class="abs contents-col" style="left:715px;top:961px"><li>Lorem ipsum dolor sit amet</li><li>Lorem ipsum dolor sit amet</li><li>Lorem ipsum dolor sit amet</li><li>Lorem ipsum dolor sit amet</li><li>Lorem ipsum dolor sit amet</li><li>Lorem ipsum dolor sit amet</li></ul>

  <div class="abs brand-mark" style="left:1015px;top:913px;width:56px;height:56px"></div>
  <div class="abs brand-name" style="left:960px;top:979px;font-size:17px">LUMORA LEARNING</div>
  <div class="abs address">01 Lorem ipsum dolor sit amet 1<br>12345 NJ Lorem ipsum dolor.<br>Phone: (+91) 98 40 215634</div>

  <div class="abs bottom-bar">© 2013 Lumora Learning</div>
</footer>

</body>
</html>
```